Gluten free flour; by LOAFMIRE

We are a specialised flour company and this project is to develop packaging for a very niche and upmarket lifestyle gluten free flour in plain and also in wholemeal ( two products and you can choose which one would you like to design and submit for review)

We believe in minimalistic yet easily acceptable Design that STANS OUT and catches the eye of the viewer on a busy shelve in a grocery store.
The product will be sold on our website, through Pellora, through Social Media and also through special campaigns together with Grainwell Alliance of Canada.

We are looking for a stand up bag with zip lock and tear notch size approx. 9 in wide x 13 inch tall x 4 inch gusset .

Our flour produces soft, pliable, moist and fluffy roti and tortillas. (Flour only not finished product).

We only manufacture Gluten free flour and flour related products and do not deal with wheat or wheat related products.

Website isn't an initial stage URL http://env.quorvane.example/loafmire Company name : Loafmire Inc

Target Market(s)

Canadian East Indian, Canadian-Latin Americans, Caucasian-Canadians and Americans who are gluten free by lifestyle choice or because of Celiac disease or Gluten Intolerance.

Industry/Entity Type

Manufacturing

Logo Text

Loafmire

Requirements
Must have
• Prominent "Gluten Free"
Emblems: 100% Organic, 100% Gluten free, Low GI, Vegan, Soy free, dairy free, allergens free, Grainwell Alliance
Roti graphics (picture)
Nice to have
• 0% Saturated Fat only 1% Total fat, Cholesterol Free, Very Low Sodium, Good Source of Dietary Fiber. Weight management. Perfect for Gluten free lifestyle. Organic ingredients
Graphics of grains (Sorghum, Buckwheat, Brown rice, Chickpeas)
Should not have
• Wheat or related to wheat graphics, Anything referring to Gluten. Too busy looking

```html
<!DOCTYPE html>
<html lang="en">
<head>
<meta charset="utf-8">
<title>Loafmire Gluten-Free Flour</title>
<link href="https://fonts.googleapis.com/css2?family=Lexend:wght@400;700&family=Source+Sans+3:wght@300;400&display=swap" rel="stylesheet">
<style>
  :root {
    --gold: #ddb355;
    --teal: #55716f;
    --ink: #4a4a4a;
    --paper: #ffffff;
    --stage: #f2f2f2;
    --frame: #8a8a8a;
  }
  html, body {
    margin: 0;
    padding: 0;
    width: 1200px;
    height: 2297px;
    overflow: hidden;
    background: var(--stage);
  }
  .label-art {
    position: absolute;
    left: 33px;
    top: 425px;
    width: 1260px;
    height: 1608px;
    background: var(--paper);
    border: 1px solid var(--frame);
    box-sizing: border-box;
    transform: scale(0.9);
    transform-origin: top left;
    overflow: hidden;
  }
  .teal-hexagon {
    position: absolute;
    left: 0;
    top: 0;
  }
  .grain-illustration {
    position: absolute;
    left: 0;
    top: 0;
    width: 450px;
    height: 860px;
    background: radial-gradient(ellipse at 45% 55%, rgba(214,170,82,0.85) 0%, rgba(222,184,105,0.55) 45%, rgba(255,255,255,0) 72%);
  }
  .roti-photo {
    position: absolute;
    left: 0;
    top: 870px;
    width: 385px;
    height: 335px;
    border-radius: 0 50% 50% 0 / 0 45% 55% 0;
    background: linear-gradient(180deg, #f3e3a8 0%, #eddba0 55%, #d9c185 100%);
  }
  .brand-name {
    position: absolute;
    left: 408px;
    top: 195px;
    width: 720px;
    margin: 0;
    text-align: center;
    font-family: "Lexend", sans-serif;
    font-weight: 700;
    font-size: 116px;
    line-height: 1;
    color: var(--gold);
    letter-spacing: 1px;
  }
  .product-title {
    position: absolute;
    left: 420px;
    top: 405px;
    width: 740px;
    margin: 0;
    text-align: center;
    font-family: "Lexend", sans-serif;
    font-weight: 400;
    font-size: 128px;
    line-height: 116px;
    color: var(--teal);
  }
  .benefit-list {
    position: absolute;
    left: 668px;
    top: 758px;
    margin: 0;
    padding: 0;
    list-style: none;
    font-family: "Source Sans 3", sans-serif;
    font-weight: 300;
    font-size: 36px;
    line-height: 57px;
    color: var(--ink);
  }
  .benefit-list li {
    position: relative;
    padding-left: 52px;
  }
  .benefit-list li::before {
    content: "";
    position: absolute;
    left: 0;
    top: 15px;
    width: 29px;
    height: 29px;
    border-radius: 50%;
    background: var(--gold);
  }
  .badge-band-shadow {
    position: absolute;
    left: 325px;
    top: 1418px;
    width: 913px;
    height: 170px;
    background: var(--teal);
  }
  .badge-band {
    position: absolute;
    left: 347px;
    top: 1438px;
    width: 913px;
    height: 170px;
    background: var(--gold);
    display: flex;
    justify-content: space-around;
    padding: 0 8px;
    box-sizing: border-box;
  }
  .badge {
    width: 140px;
    display: flex;
    flex-direction: column;
    align-items: center;
    padding-top: 25px;
  }
  .badge svg {
    width: 92px;
    height: 92px;
    display: block;
  }
  .badge-label {
    margin-top: 12px;
    font-family: "Source Sans 3", sans-serif;
    font-weight: 400;
    font-size: 23px;
    color: #3a3a3a;
    white-space: nowrap;
  }
</style>
</head>
<body>
  <main class="label-art">
    <svg class="teal-hexagon" width="460" height="1608" viewBox="0 0 460 1608" aria-hidden="true">
      <polygon points="0,473 408,713 408,1193 0,1423" fill="var(--teal)"/>
    </svg>
    <div class="grain-illustration" role="img" aria-label="Illustration of golden grain stalks and rice panicles"></div>
    <div class="roti-photo" role="img" aria-label="Photo of a stack of soft roti flatbreads"></div>

    <h1 class="brand-name">LOAFMIRE</h1>
    <h2 class="product-title">Gluten-Free<br>Flour</h2>

    <ul class="benefit-list">
      <li>0% Saturated Fat only 1% Total fat</li>
      <li>Cholesterol Free</li>
      <li>Very Low Sodium</li>
      <li>Good Source of Dietary Fiber</li>
      <li>Weight management</li>
      <li>Perfect for Gluten free lifestyle</li>
      <li>Organic ingredients</li>
    </ul>

    <div class="badge-band-shadow"></div>
    <div class="badge-band">
      <div class="badge">
        <svg viewBox="0 0 92 92" fill="none" stroke="#3a3a3a" stroke-width="2">
          <circle cx="46" cy="46" r="43"/>
          <rect x="36" y="30" width="20" height="36" rx="4"/>
          <line x1="38" y1="24" x2="54" y2="24"/>
          <line x1="18" y1="18" x2="74" y2="74"/>
        </svg>
        <span class="badge-label">DAIRY FREE</span>
      </div>
      <div class="badge">
        <svg viewBox="0 0 92 92" fill="none" stroke="#3a3a3a" stroke-width="2">
          <circle cx="46" cy="46" r="43"/>
          <ellipse cx="46" cy="46" rx="12" ry="26" transform="rotate(45 46 46)"/>
          <circle cx="38" cy="54" r="5"/>
          <circle cx="54" cy="38" r="5"/>
          <line x1="18" y1="18" x2="74" y2="74"/>
        </svg>
        <span class="badge-label">SOY FREE</span>
      </div>
      <div class="badge">
        <svg viewBox="0 0 92 92" fill="none" stroke="#3a3a3a" stroke-width="2">
          <circle cx="46" cy="46" r="43"/>
          <circle cx="46" cy="34" r="9"/>
          <line x1="46" y1="43" x2="46" y2="70"/>
          <path d="M46 62 C38 56 32 58 30 64"/>
          <path d="M46 62 C54 56 60 58 62 64"/>
        </svg>
        <span class="badge-label">100% ORGANIC</span>
      </div>
      <div class="badge">
        <svg viewBox="0 0 92 92" fill="none" stroke="#3a3a3a" stroke-width="2">
          <circle cx="46" cy="46" r="43"/>
          <line x1="46" y1="30" x2="46" y2="70"/>
          <path d="M46 52 C36 50 28 42 28 34 C38 36 44 42 46 52"/>
          <path d="M46 52 C56 50 64 42 64 34 C54 36 48 42 46 52"/>
        </svg>
        <span class="badge-label">VEGAN</span>
      </div>
      <div class="badge">
        <svg viewBox="0 0 92 92" fill="none" stroke="#3a3a3a" stroke-width="2">
          <circle cx="46" cy="46" r="43"/>
          <line x1="46" y1="24" x2="46" y2="72"/>
          <ellipse cx="40" cy="36" rx="5" ry="8"/>
          <ellipse cx="52" cy="36" rx="5" ry="8"/>
          <ellipse cx="40" cy="52" rx="5" ry="8"/>
          <ellipse cx="52" cy="52" rx="5" ry="8"/>
          <line x1="18" y1="18" x2="74" y2="74"/>
        </svg>
        <span class="badge-label">GLUTEN FREE</span>
      </div>
      <div class="badge">
        <svg viewBox="0 0 92 92" fill="none" stroke="#3a3a3a" stroke-width="2">
          <circle cx="46" cy="46" r="43"/>
          <path d="M28 40 Q46 34 64 40 L60 62 Q46 68 32 62 Z"/>
          <text x="46" y="58" text-anchor="middle" font-family="Source Sans 3, sans-serif" font-size="18" fill="#3a3a3a" stroke="none">GI</text>
        </svg>
        <span class="badge-label">LOW GI</span>
      </div>
    </div>
  </main>
</body>
</html>
```